40-year-old commercial construction firm :: Business Card Revamp

We are a 40 year-old, private general construction company based in Dallas, Texas, and we are considering updating our business cards, which could lead to a larger "brand refresh" campaign.

We work in a competitive environment, selling to business owners and executives making large scale purchasing decisions on behalf of their firms. A majority of our business is repeat business, with a long sales-cycle; while business can be difficult to identify and land, the effort is often rewarded with multiple projects.

We are open to a logo "refresh" as well as designs that incorporate the existing logo.

Target Market(s)

B2B selling to business owners/executives/end users who make facility decisions for their firms.

Industry/Entity Type

Construction Company

Contact Information for Business Card

Refresh from the example provided

Logo Text

Tarnell Building Company :: See card example

Font styles to use
Other font styles liked:
• See sample card :: Designers to choose

Colors

Designer to choose colors to be used in the design.

Requirements
Must have
• Design should convey:
• Confidence
• Competence
• Capability
• Stability
• Tagline: Genuine Relationships :: Superior Services :: Environmentally Aware
Nice to have
• A solid design that is transferable from print to online.
• Note that we are also considering a painted-edge printing / card design
Should not have
• Too much color or whimsy. Our clients tend to be the serious type, and we work hard to present a serious, professional presence in the marketplace.

```html
<!DOCTYPE html>
<html lang="en">
<head>
<meta charset="utf-8">
<title>Tarnell Building Company – Business Card</title>
<link rel="stylesheet" href="https://fonts.googleapis.com/css2?family=Open+Sans:wght@400;600&family=Work+Sans:wght@400;600&display=swap">
<style>
  :root {
    --backdrop: #2a2a2b;
    --card: #1c1c1d;
    --card-edge: #111112;
    --gold: #c9a21a;
    --white: #f2f2f2;
    --silver: #d6d6d6;
    --muted: #e6e6e6;
  }
  * { margin: 0; padding: 0; box-sizing: border-box; }
  html, body {
    width: 1200px; height: 900px; overflow: hidden;
    background: var(--backdrop);
  }
  .canvas {
    width: 1200px; height: 900px;
    display: flex; flex-direction: column;
    align-items: center; justify-content: center;
    gap: 44px;
  }
  .card {
    position: relative;
    width: 700px; height: 400px;
    background: var(--card);
    border: 1px solid var(--card-edge);
    box-shadow: 0 10px 30px rgba(0,0,0,.45);
  }

  /* Front */
  .card-front {
    display: flex; flex-direction: column;
    align-items: center; justify-content: center;
  }
  .front-mark {
    display: flex; align-items: center; gap: 16px;
  }
  .front-mark .dot {
    width: 34px; height: 34px; border-radius: 50%;
    background: var(--silver);
  }
  .front-mark .wordmark {
    font-family: "Open Sans", sans-serif;
    font-weight: 400; font-size: 52px;
    color: var(--silver);
    letter-spacing: 1px;
    line-height: 1.2;
  }
  .tagline {
    position: absolute; left: 0; right: 0; bottom: 34px;
    text-align: center;
    font-family: "Work Sans", sans-serif;
    font-weight: 400; font-size: 12px;
    letter-spacing: 1.5px; text-transform: uppercase;
    color: var(--gold);
  }

  /* Back */
  .brand {
    position: absolute; left: 70px; top: 150px;
    display: flex; align-items: flex-start; gap: 14px;
  }
  .brand .dot {
    width: 44px; height: 44px; border-radius: 50%;
    background: var(--gold); margin-top: 6px;
  }
  .brand-name {
    font-family: "Open Sans", sans-serif; font-weight: 400;
    color: var(--white); line-height: 1;
  }
  .brand-name .primary { display: block; font-size: 44px; }
  .brand-name .secondary { display: block; font-size: 13px; letter-spacing: .5px; margin-top: 6px; }

  .divider {
    position: absolute; left: 340px; top: 110px;
    width: 2px; height: 185px; background: var(--white);
  }
  .contact {
    position: absolute; left: 372px; top: 112px;
    font-family: "Work Sans", sans-serif; color: var(--muted);
  }
  .contact .person {
    font-weight: 600; font-size: 27px; letter-spacing: 3px;
    color: var(--gold); text-transform: uppercase; line-height: 1;
  }
  .contact .role { font-size: 15px; margin-top: 4px; }
  .contact .address { font-size: 16px; line-height: 1.3; margin-top: 10px; }
  .contact-list { list-style: none; margin-top: 8px; }
  .contact-list li {
    display: flex; align-items: center; gap: 14px;
    font-size: 16.5px; line-height: 1.4;
  }
  .contact-list svg { width: 11px; height: 11px; flex: none; }
</style>
</head>
<body>
<main class="canvas">

  <section class="card card-front" aria-label="Card front">
    <div class="front-mark">
      <span class="dot"></span>
      <span class="wordmark">Tarnell</span>
    </div>
    <p class="tagline">Genuine Relationships :: Superior Services :: Environmentally Aware</p>
  </section>

  <section class="card card-back" aria-label="Card back">
    <div class="brand">
      <span class="dot"></span>
      <div class="brand-name">
        <span class="primary">Tarnell</span>
        <span class="secondary">BUILDING COMPANY, LTD</span>
      </div>
    </div>

    <div class="divider"></div>

    <div class="contact">
      <p class="person">Marcus Hale</p>
      <p class="role">Director</p>
      <p class="address">480 Commerce Parkway,<br>Suite 210, Dallas, TX</p>
      <ul class="contact-list">
        <li>
          <svg viewBox="0 0 12 12" fill="none" stroke="#c9a21a" stroke-width="1.4"><rect x="3" y="1" width="6" height="10" rx="1"/><line x1="5" y1="9" x2="7" y2="9"/></svg>
          +1 214 555 0140
        </li>
        <li>
          <svg viewBox="0 0 12 12" fill="#c9a21a"><path d="M2.5 1 L4.5 1 L5 3.5 L3.8 4.5 Q5 7 7.5 8.2 L8.5 7 L11 7.5 L11 9.5 Q11 11 9.5 11 Q1 10 1 2.5 Q1 1 2.5 1Z"/></svg>
          +1 214 555 0188
        </li>
        <li>
          <svg viewBox="0 0 12 12" fill="none" stroke="#c9a21a" stroke-width="1.3"><rect x="1" y="2.5" width="10" height="7"/><polyline points="1,2.5 6,6.5 11,2.5"/></svg>
          info@tarnellbuilding.com
        </li>
        <li>
          <svg viewBox="0 0 12 12" fill="none" stroke="#c9a21a" stroke-width="1.2"><circle cx="6" cy="6" r="5"/><ellipse cx="6" cy="6" rx="2.2" ry="5"/><line x1="1" y1="6" x2="11" y2="6"/></svg>
          www.tarnellbuilding.com
        </li>
      </ul>
    </div>
  </section>

</main>
</body>
</html>
```